BrivoLane Ute.

I want the full logo on one side. And the other side the card if right Ralf the logo the left half orange like the car in the logo color with Danielle R Morrow
Founder and CEO
Email symbol then dmorrow@brivolaneute.com
Www symbol. Then Brivolaneute.com
Phone symbol then 413-926-BRIV
The very bottom would like Brivo Lane Ute is a division of Harmond Vistas. LLC

```html
<!DOCTYPE html>
<html lang="en">
<head>
<meta charset="utf-8">
<title>Brivo Lane Ute – Business Card</title>
<link rel="stylesheet" href="https://fonts.googleapis.com/css2?family=Open+Sans:wght@400;600&display=swap">
<style>
  :root {
    --backdrop: #ecebe8;
    --card: #ffffff;
    --ink: #111111;
    --ink-soft: #222222;
    --accent: #e8901f;
    --card-shadow: 0 4px 10px rgba(0, 0, 0, 0.25);
  }
  * { box-sizing: border-box; margin: 0; padding: 0; }
  html, body {
    width: 1200px;
    height: 1000px;
    overflow: hidden;
    background: var(--backdrop);
    font-family: "Open Sans", Arial, sans-serif;
    color: var(--ink);
  }
  .canvas {
    position: relative;
    width: 1200px;
    height: 1000px;
  }
  .card {
    position: absolute;
    left: 187px;
    width: 827px;
    background: var(--card);
    box-shadow: var(--card-shadow);
  }
  .card--front { top: 14px; height: 473px; }
  .card--back  { top: 505px; height: 472px; }

  .brand {
    position: absolute;
    display: flex;
    align-items: center;
    gap: 14px;
  }
  .brand__mark {
    width: 26px;
    height: 26px;
    background: var(--accent);
    flex: none;
  }
  .brand__name {
    font-weight: 600;
    font-size: 40px;
    color: var(--ink);
    white-space: nowrap;
    letter-spacing: 0.5px;
  }
  .card--front .brand { left: 50px; top: 208px; }
  .card--back .brand { left: 50%; top: 50%; transform: translate(-50%, -50%); }

  .person {
    position: absolute;
    left: 538px;
    top: 114px;
  }
  .person__name {
    font-size: 31px;
    font-weight: 400;
    line-height: 1.1;
    color: var(--ink);
  }
  .person__role {
    font-size: 17px;
    line-height: 1.3;
    margin-left: 2px;
    color: var(--ink-soft);
  }

  .contacts {
    position: absolute;
    left: 540px;
    top: 222px;
    list-style: none;
  }
  .contacts__item {
    position: absolute;
    left: 0;
    display: flex;
    align-items: center;
    gap: 12px;
    font-size: 15px;
    color: var(--ink-soft);
    white-space: nowrap;
  }
  .contacts__item--email { top: 0; }
  .contacts__item--web   { top: 49px; }
  .contacts__item--phone { top: 106px; }
  .contacts__icon {
    width: 20px;
    height: 20px;
    flex: none;
  }

  .legal {
    position: absolute;
    left: 0;
    right: 0;
    top: 424px;
    padding-left: 87px;
    text-align: center;
    font-size: 14.5px;
    color: var(--ink-soft);
  }
</style>
</head>
<body>
<main class="canvas">

  <section class="card card--front" aria-label="Card front">
    <div class="brand">
      <span class="brand__mark"></span>
      <span class="brand__name">Brivo Lane Ute</span>
    </div>

    <div class="person">
      <h1 class="person__name">Danielle R Morrow</h1>
      <p class="person__role">Founder and CEO</p>
    </div>

    <ul class="contacts">
      <li class="contacts__item contacts__item--email">
        <svg class="contacts__icon" viewBox="0 0 20 20" fill="none" stroke="#222" stroke-width="1.3" aria-hidden="true">
          <rect x="2" y="5" width="16" height="11"/>
          <path d="M2 5l8 6 8-6M2 16l6-5M18 16l-6-5"/>
        </svg>
        <span>dmorrow@brivolaneute.com</span>
      </li>
      <li class="contacts__item contacts__item--web">
        <svg class="contacts__icon" viewBox="0 0 20 20" fill="none" stroke="#222" stroke-width="1.2" aria-hidden="true">
          <circle cx="10" cy="10" r="7.5"/>
          <ellipse cx="10" cy="10" rx="3.2" ry="7.5"/>
          <path d="M2.5 10h15M3.7 6h12.6M3.7 14h12.6"/>
        </svg>
        <span>Brivolaneute.com</span>
      </li>
      <li class="contacts__item contacts__item--phone">
        <svg class="contacts__icon" viewBox="0 0 20 20" fill="none" stroke="#222" stroke-width="1.5" aria-hidden="true">
          <circle cx="10" cy="10" r="8.5"/>
          <path d="M7 5.5l1.6 2.3-1 1.2c.6 1.3 1.5 2.2 2.8 2.8l1.2-1 2.3 1.6-.9 1.6c-3.4-.4-6.1-3.1-6.5-6.5z" fill="#222"/>
        </svg>
        <span>413-926-BRIV</span>
      </li>
    </ul>

    <p class="legal">Brivo Lane Ute is a division of Harmond Vistas. LLC</p>
  </section>

  <section class="card card--back" aria-label="Card back">
    <div class="brand">
      <span class="brand__mark"></span>
      <span class="brand__name">Brivo Lane Ute</span>
    </div>
  </section>

</main>
</body>
</html>
```